Postcard Design for Silent Harbors

This will be a promotional postcard, 4 x 6 inches, to be sent, to let fans know about my next book. The cover art should be in color on one side; the copy for the back should be on half of the space (so there is room for an address. I've attached suggested copy. If I've given you too many words, please contact me.
Thank you -- Ivy

I love both designs so far! One comment: Even if the type is small, I'd like a return address on the cards so I can keep my mailing list up-to-date. The address is P.O. Box 871, Alderport, Vermont 04712 Thank you!

```html
<!DOCTYPE html>
<html lang="en">
<head>
<meta charset="utf-8">
<title>Silent Harbors – Promotional Postcard</title>
<link rel="stylesheet" href="https://fonts.googleapis.com/css2?family=Cinzel+Decorative:wght@700&family=Dancing+Script:wght@500&family=Mulish:wght@400;600&display=swap">
<style>
  :root {
    --page-bg: #f4f3f1;
    --card-left: #f1e3a9;
    --card-mid: #e6dccb;
    --card-right: #dcd5ec;
    --ink-purple: #4b2c8c;
    --ink-soft: #6a5a86;
    --ink-grey: #675f73;
    --ribbon: #e86ea7;
    --ribbon-dark: #c24e86;
    --ribbon-fold: #a83a70;
    --rule: #7a62b8;
    --divider: #b9b0c4;
    --stamp-line: #ffffff;
  }
  * { box-sizing: border-box; margin: 0; padding: 0; }
  html, body {
    width: 1200px; height: 1000px; overflow: hidden;
    background: var(--page-bg);
  }
  .postcard {
    position: absolute; left: 50px; top: 75px;
    width: 1100px; height: 850px;
    background: linear-gradient(90deg, var(--card-left) 0%, var(--card-mid) 50%, var(--card-right) 100%);
    box-shadow: 0 6px 18px rgba(0,0,0,0.18);
    font-family: "Mulish", sans-serif;
  }
  .series-ribbon { position: absolute; left: 40px; top: 58px; width: 470px; height: 72px; }
  .series-ribbon__label {
    position: absolute; left: 50px; top: 10px; width: 370px; height: 40px;
    display: flex; align-items: center; justify-content: center;
    color: #fff; font-size: 22px; font-weight: 400; letter-spacing: 0.2px;
  }
  .series-ribbon__label strong { font-weight: 600; margin: 0 6px; }
  .book-title {
    position: absolute; left: 118px; top: 140px;
    font-family: "Cinzel Decorative", serif; font-weight: 700;
    color: var(--ink-purple); font-size: 58px; line-height: 64px;
    text-shadow: 0 0 6px rgba(255,255,255,0.9);
  }
  .book-title span { display: block; }
  .book-title span + span { padding-left: 40px; }
  .series-name {
    position: absolute; left: 72px; top: 310px;
    font-family: "Dancing Script", cursive; font-weight: 500;
    color: var(--ink-purple); font-size: 36px;
  }
  .blurb {
    position: absolute; left: 76px; top: 395px; width: 460px;
    color: var(--ink-purple); font-size: 20px; line-height: 30px;
  }
  .book-details {
    position: absolute; left: 80px; top: 605px;
    color: var(--ink-grey); font-size: 17px; line-height: 21px;
  }
  .book-details strong { font-weight: 600; }
  .divider {
    position: absolute; left: 560px; top: 160px;
    width: 2px; height: 545px; background: var(--divider);
  }
  .return-address {
    position: absolute; left: 605px; top: 55px;
    color: var(--ink-soft); font-size: 17px; line-height: 22px; font-style: normal;
  }
  .stamp-box {
    position: absolute; left: 882px; top: 48px; width: 145px; height: 162px;
    border: 1.5px solid var(--stamp-line); border-radius: 8px;
  }
  .address-lines { position: absolute; left: 620px; top: 312px; width: 415px; }
  .address-lines li {
    list-style: none; height: 57px; border-bottom: 1.5px solid var(--rule);
  }
  .address-lines li:first-child { height: 0; }
</style>
</head>
<body>
  <article class="postcard">
    <div class="series-ribbon">
      <svg width="470" height="72" viewBox="0 0 470 72" aria-hidden="true">
        <polygon points="0,22 52,22 52,66 0,66 16,44" fill="var(--ribbon-dark)"/>
        <polygon points="470,22 418,22 418,66 470,66 454,44" fill="var(--ribbon-dark)"/>
        <polygon points="52,52 66,52 52,66" fill="var(--ribbon-fold)"/>
        <polygon points="418,52 404,52 418,66" fill="var(--ribbon-fold)"/>
        <rect x="50" y="8" width="370" height="44" fill="var(--ribbon)"/>
      </svg>
      <div class="series-ribbon__label"><strong>1st</strong> in <strong>new</strong> IVY WREN series!</div>
    </div>

    <h1 class="book-title"><span>SILENT</span><span>HARBORS</span></h1>
    <h2 class="series-name">Coastal Stitches Mystery Series</h2>

    <p class="blurb">Maggie Collins returns to her Maine home town with P.I. experience and a gun, vowing to find her mother’s killer. Then the shady agent for her grandmother’s custom needlepoint business also dies, clues tie his murder to her mother’s: and Maggie and her grandmother are both suspects.</p>

    <p class="book-details">
      Harrow Lane Publishing<br>
      ISBN 978-0-00000-871-2<br>
      Mass Market paperback $7.00<br>
      + e-book formats<br>
      Visit Ivy at www.Ivywren.com &amp;<br>
      friend her on <strong>Pagebook</strong> and <strong>Readshelf</strong>
    </p>

    <div class="divider"></div>

    <address class="return-address">
      (Return Address)<br>
      Post Office Box 871<br>
      Alderport,<br>
      Vermont 04712
    </address>

    <div class="stamp-box"></div>

    <ul class="address-lines">
      <li></li><li></li><li></li><li></li><li></li><li></li><li></li>
    </ul>
  </article>
</body>
</html>
```